Vantor Business Card Design

We need a business card design for a new company in NJ called Vantor LLC. We provide plumbing, sewer & drain cleaning, and full bath remodeling services. We need a logo design that will be used for several applications such as; cards, stickers, t shirts, and truck lettering. The company hopes to one day be a full service operation offering plumbing, heating, cooling, electric, so we need a design that is very general (aka no pipe wrenches). Colors will be royal blue,neon lime green, and would like to add diamond plate or steel plate to give it a very masculine feel and look.

Contact Information for Business Card

Vantor LLC. ,Plumbing, Sewer & Drain Cleaning, Bath Remodeling
North Brunswick, NJ 08902
609.424.7316
Vantorplumbinghelp.example
Info@vantorplumbinghelp.example
Stay calm, ring vantor!, Rick Tembley- President
NJ Master Plumbing License: 58627, Residential & Commercial Service

Requirements
Should not have
• Tool icons
Script font

```html
<!DOCTYPE html>
<html lang="en">
<head>
<meta charset="utf-8">
<title>Vantor LLC – Business Card</title>
<link rel="stylesheet" href="https://fonts.googleapis.com/css2?family=Exo+2:wght@300;400;600&display=swap">
<style>
  :root {
    --stage: #e7e4df;
    --brand-blue: #1fb0ec;
    --charcoal: #2a2a2c;
    --steel-light: #f7f7f7;
    --steel-dark: #c6c6c6;
    --white: #ffffff;
  }
  html, body {
    margin: 0;
    padding: 0;
    overflow: hidden;
  }
  .canvas {
    position: relative;
    width: 1200px;
    height: 970px;
    background: var(--stage);
    overflow: hidden;
    font-family: "Exo 2", sans-serif;
  }
  .card {
    position: absolute;
    width: 760px;
    height: 434px;
    box-shadow: 0 10px 28px rgba(0,0,0,0.22);
  }
  .card svg { display: block; width: 100%; height: 100%; }
  .card-back  { left: 90px;  top: 50px; }
  .card-front { left: 350px; top: 486px; }

  .wordmark { font-family: "Exo 2", sans-serif; font-weight: 300; fill: var(--brand-blue); }
  .web-strip-text { font-family: "Exo 2", sans-serif; font-weight: 400; fill: var(--white); letter-spacing: 3px; }
  .person-name { font-family: "Exo 2", sans-serif; font-weight: 600; fill: var(--white); letter-spacing: 2px; }
  .person-role { font-family: "Exo 2", sans-serif; font-weight: 400; fill: var(--white); letter-spacing: 1.5px; }
  .contact-line { font-family: "Exo 2", sans-serif; font-weight: 400; fill: var(--white); letter-spacing: 1px; }
  .icon-ring { fill: none; stroke: var(--white); stroke-width: 1.6; }
  .icon-glyph { fill: var(--white); }
  .icon-stroke { fill: none; stroke: var(--white); stroke-width: 1.4; }
</style>
</head>
<body>
<div class="canvas">

  <!-- Card back -->
  <div class="card card-back">
    <svg viewBox="0 0 760 434" xmlns="http://www.w3.org/2000/svg">
      <defs>
        <linearGradient id="steelBack" x1="0" y1="0" x2="0" y2="1">
          <stop offset="0" stop-color="var(--steel-light)"/>
          <stop offset="1" stop-color="var(--steel-dark)"/>
        </linearGradient>
      </defs>
      <rect class="back-base" width="760" height="434" fill="var(--brand-blue)"/>
      <rect class="back-web-strip" x="0" y="118" width="760" height="34" fill="var(--charcoal)"/>
      <text class="web-strip-text" x="730" y="141" font-size="17" text-anchor="end">www.vantorsite.example</text>
      <rect class="back-steel-band" x="0" y="152" width="760" height="176" fill="url(#steelBack)"/>
      <path class="back-tab" d="M120 152 Q130 196 175 196 L300 196 Q345 196 355 152 Z" fill="var(--charcoal)"/>
      <text class="wordmark" x="400" y="290" font-size="64" text-anchor="middle">Vantor LLC</text>
      <rect class="back-rule" x="0" y="328" width="760" height="10" fill="var(--charcoal)"/>
    </svg>
  </div>

  <!-- Card front -->
  <div class="card card-front">
    <svg viewBox="0 0 760 434" xmlns="http://www.w3.org/2000/svg">
      <defs>
        <linearGradient id="steelFront" x1="0" y1="0" x2="0" y2="1">
          <stop offset="0" stop-color="var(--steel-light)"/>
          <stop offset="1" stop-color="var(--steel-dark)"/>
        </linearGradient>
      </defs>
      <rect class="front-base" width="760" height="434" fill="var(--brand-blue)"/>
      <path class="front-steel-panel" d="M0 0 L560 0 L640 210 L0 210 Z" fill="url(#steelFront)"/>
      <path class="front-divider" d="M560 0 L640 210" stroke="var(--charcoal)" stroke-width="8"/>
      <path class="front-tab" d="M470 210 Q480 168 525 168 L600 168 Q622 168 632 190 L640 210 Z" fill="var(--charcoal)"/>
      <rect class="corner-tab" x="690" y="92" width="90" height="26" rx="10" fill="var(--steel-light)"/>
      <text class="wordmark" x="48" y="150" font-size="70">Vantor LLC</text>

      <path class="name-bar" d="M0 210 L470 210 L452 246 L0 246 Z" fill="var(--charcoal)"/>
      <text x="24" y="236">
        <tspan class="person-name" font-size="19">DALE MORROW</tspan>
        <tspan class="person-role" font-size="14" dx="10">|  GENERAL MANAGER</tspan>
      </text>

      <!-- contact column left -->
      <g class="contact-item" transform="translate(34 290)">
        <circle class="icon-ring" r="10"/>
        <path class="icon-glyph" d="M-4.5 -5 q-1.5 1 0 4 q3 5 7 6.5 q2.5 0.5 3 -1.5 l-2.5 -2 l-1.5 1 q-2.5 -1.5 -4 -4 l1 -1.5 l-2 -2.5 z"/>
      </g>
      <text class="contact-line" x="54" y="295" font-size="14">555 018 2744</text>

      <g class="contact-item" transform="translate(34 328)">
        <circle class="icon-ring" r="10"/>
        <rect class="icon-stroke" x="-3.5" y="-6" width="7" height="12" rx="1.2"/>
      </g>
      <text class="contact-line" x="54" y="333" font-size="14">555 018 2744</text>

      <g class="contact-item" transform="translate(34 366)">
        <circle class="icon-ring" r="10"/>
        <path class="icon-glyph" d="M0 -6.5 a4.5 4.5 0 0 1 4.5 4.5 q0 3 -4.5 8.5 q-4.5 -5.5 -4.5 -8.5 a4.5 4.5 0 0 1 4.5 -4.5 z M0 -3.8 a1.8 1.8 0 1 0 0.01 0 z" fill-rule="evenodd"/>
      </g>
      <text class="contact-line" x="54" y="371" font-size="14">42 Elm Park Road  3rd Floor Suite 5</text>

      <!-- contact column right -->
      <g class="contact-item" transform="translate(300 290)">
        <circle class="icon-ring" r="10"/>
        <rect class="icon-stroke" x="-5.5" y="-4" width="11" height="8" rx="1"/>
        <path class="icon-stroke" d="M-5.5 -4 L0 0.8 L5.5 -4"/>
      </g>
      <text class="contact-line" x="320" y="295" font-size="14">hello@vantormail.example</text>

      <g class="contact-item" transform="translate(300 328)">
        <circle class="icon-ring" r="10"/>
        <circle class="icon-stroke" r="6"/>
        <ellipse class="icon-stroke" rx="2.6" ry="6"/>
        <path class="icon-stroke" d="M-6 0 H6"/>
      </g>
      <text class="contact-line" x="320" y="333" font-size="14">www.vantorsite.example</text>
    </svg>
  </div>

</div>
</body>
</html>
```